Sleek and eye catching flyer design required for LIGHT SOUND & SPECIAL EFFECTS COMPANY!

Company: BrivOra Lamp & Tone

we provide lights, audio visual and indoor & outdoor pyrotechnics for events & occasions, specialising in Weddings.
Visit www.brivoralt.com.au for more details on our product and service.

Flyers should be DL double sided. Background can be in white or black.
Include the following:
We Specialise in:
- professional dynamic audio speaker system
- wedding uplights decor design
- professional disco dance/stage lights
- full hd projectors & screen
- professional dry ice fog effect
- professional indoor & outdoor fireworks
- traditional chinese firecrackers
- wedding initial letter lights
- 2.4m Heart arch light
And much more....

Also include contact details :
mobile: 0467152938
Email: info@brivoralt.com.au
Website: www.brivoralt.com.au
Address: 517 Palmcourt Road, Elmvale VIC 3158.

Please email if you beed more info.

Target Market(s)

Wedding industry

Industry/Entity Type

Wedding

Font styles to use
Serif

Requirements
Must have
• LOGO,
• PHOTOs

```html
<!DOCTYPE html>
<html lang="en">
<head>
<meta charset="utf-8">
<title>BrivOra Lamp &amp; Tone – Flyer</title>
<link href="https://fonts.googleapis.com/css2?family=Great+Vibes&family=Tinos:wght@400;700&display=swap" rel="stylesheet">
<style>
  :root {
    --ink: #000000;
    --paper: #ffffff;
    --soft: #e9e9e9;
    --strip: #dcdcdc;
    --strip-text: #1a1a1a;
    --photo-a: #3a2a3a;
    --photo-b: #b58aa8;
    --photo-c: #f1dfe8;
  }
  * { margin: 0; padding: 0; box-sizing: border-box; }
  html, body { width: 1200px; height: 2464px; overflow: hidden; background: var(--ink); }
  .flyer {
    position: relative; width: 1200px; height: 2464px;
    background: var(--ink); color: var(--paper);
    font-family: "Tinos", "Times New Roman", serif;
  }
  .mission {
    position: absolute; top: 40px; left: 60px; right: 60px;
    font-family: "Great Vibes", cursive;
    font-size: 60px; line-height: 100px; text-align: center; color: var(--soft);
  }
  .services-heading {
    position: absolute; top: 484px; left: 0; right: 0;
    text-align: center; font-size: 42px; letter-spacing: 1px;
  }
  .services {
    position: absolute; top: 592px; left: 120px; right: 80px;
    list-style: none; font-size: 44px; line-height: 66px; text-transform: uppercase;
  }
  .services li { padding-left: 30px; position: relative; }
  .services li::before { content: "•"; position: absolute; left: 0; }
  .services .more { padding-left: 320px; }
  .services .more::before { content: none; }
  .cta {
    position: absolute; top: 1470px; left: 0; right: 0;
    text-align: center; font-family: "Great Vibes", cursive; font-size: 76px;
  }
  .contact {
    position: absolute; top: 1620px; left: 0; right: 0;
    text-align: center; font-size: 44px; letter-spacing: 5px; line-height: 92px;
  }
  .social {
    position: absolute; top: 1916px; left: 0; right: 0;
    display: flex; justify-content: center; gap: 48px;
  }
  .social span { width: 78px; height: 78px; border-radius: 50%; background: var(--paper); }
  .event-photo {
    position: absolute; top: 2068px; left: 0; width: 1200px; height: 330px;
    background: radial-gradient(ellipse at 50% 35%, var(--photo-c) 0%, var(--photo-b) 40%, var(--photo-a) 100%);
  }
  .address {
    position: absolute; top: 2398px; left: 0; width: 1200px; height: 66px;
    background: var(--strip); color: var(--strip-text);
    text-align: center; font-weight: 700; font-size: 40px; line-height: 66px; text-transform: uppercase;
  }
</style>
</head>
<body>
<main class="flyer">
  <p class="mission">Our goal is to exceed our customers expectations through continuous improvement in quality, services, productivity and creativity.</p>

  <h2 class="services-heading">WE SPECIALISE IN:</h2>
  <ul class="services">
    <li>Professional dynamic audio<br>speaker system</li>
    <li>Wedding uplights decor design</li>
    <li>Professional disco dance/stage<br>lights</li>
    <li>Full HD projectors &amp; screen</li>
    <li>Professional dry ice fog effect</li>
    <li>Professional indoor &amp; outdoor<br>fireworks</li>
    <li>Traditional Chinese firecrackers</li>
    <li>Wedding initial letter lights</li>
    <li>2.4m heart arch light</li>
    <li class="more">And much more....</li>
  </ul>

  <p class="cta">Contact Us Today For a Quote</p>

  <div class="contact">
    <p>046-715-2938</p>
    <p>INFO@BRIVORALT.COM.AU</p>
    <p>WWW.BRIVORALT.COM.AU</p>
  </div>

  <div class="social" aria-label="Social media links"><span></span><span></span></div>

  <div class="event-photo" role="img" aria-label="Photo of a wedding reception hall with a couple dancing under lights and fireworks"></div>

  <p class="address">517 Palmcourt Road, Elmvale VIC 3158.</p>
</main>
</body>
</html>
```